Core Values Banner For Hearthwell Partners Inc

We want to take the core values for our small growing chimney service company and post them for our entire team to see on a daily basis. We want to be remind everyone how important this is too us all. IntegrityWe try to be honest and accountable in all aspects of our business, as well as in our personal interactions. We do what we say we will do, when we say we will do it, and how we say we will do it.Kaizen“Change for the best”We strive to constantly grow and improve, both personally and professionally. We own up to our mistakes and strive to resolve and learn from them. We actively seek feedback from our clients and each other. We believe the most innovative ideas come when we intentionally look for them.FamilyWe are a family-owned business, and we consider everyone who works here and every one we serve to be part of the family. Being honest and genuine with each other and our customers is what sets us apart. We put ourselves in our customer’s shoes and make recommendations as if it were our chimney, our home and our family.

Font styles to use
Serif
Sans Serif

Colors
ec1f27

Requirements
Must have
• This banner will be approximately 2.5' in height and 6 to 6.5' in width.
• I would like all 3 core values and there definitions listed on the banner
• check out the feel of our marketing on our website www.hearthwellpartnersvt.example

```html
<!DOCTYPE html>
<html lang="en">
<head>
<meta charset="utf-8">
<title>Hearthwell Partners Inc – Core Values Banner</title>
<link rel="stylesheet" href="https://fonts.googleapis.com/css2?family=Raleway:wght@500&family=Tinos:wght@400&display=swap">
<style>
  :root {
    --brand-red: #ec1f27;
    --ink: #1a1a1a;
    --charcoal: #3a3a3a;
    --paper: #ffffff;
    --frame: #555555;
    --flame-yellow: #f7c531;
    --flame-orange: #f0761f;
    --torch-gold: #e9a93a;
  }
  * { margin: 0; padding: 0; box-sizing: border-box; }
  html, body {
    width: 1200px;
    height: 401px;
    overflow: hidden;
    background: var(--paper);
  }
  .banner {
    position: relative;
    width: 1200px;
    height: 401px;
    background: var(--paper);
    border: 1px solid var(--frame);
    overflow: hidden;
  }
  .value {
    position: absolute;
  }
  .value-title {
    font-family: "Raleway", sans-serif;
    font-weight: 500;
    font-size: 23px;
    color: var(--brand-red);
    line-height: 1.1;
    margin-bottom: 4px;
  }
  .value-text {
    font-family: "Tinos", serif;
    font-size: 14px;
    line-height: 18.5px;
    color: var(--ink);
  }
  .value--integrity { left: 60px; top: 52px; width: 270px; }
  .value--change    { left: 333px; top: 128px; width: 290px; }
  .value--family    { left: 638px; top: 221px; width: 330px; }

  .company-name {
    position: absolute;
    left: 62px;
    top: 302px;
    display: flex;
    align-items: center;
    gap: 14px;
  }
  .company-name__square {
    width: 44px;
    height: 44px;
    background: var(--charcoal);
  }
  .company-name__text {
    font-family: "Tinos", serif;
    font-size: 24px;
    letter-spacing: 2px;
    text-transform: uppercase;
    color: var(--charcoal);
  }

  .torch-art {
    position: absolute;
    left: 1040px;
    top: 14px;
    width: 126px;
    height: 364px;
    border-radius: 60px 60px 14px 14px;
    background: linear-gradient(to bottom, var(--flame-yellow) 0%, var(--flame-orange) 28%, var(--torch-gold) 55%, var(--torch-gold) 100%);
  }
</style>
</head>
<body>
  <main class="banner">
    <section class="value value--integrity">
      <h2 class="value-title">Integrity</h2>
      <p class="value-text">We try to be honest and accountable in all aspects of our business, as well as in our personal interactions. We do what we say we will do, when we say we will do it, and how we say we will do it.</p>
    </section>

    <section class="value value--change">
      <h2 class="value-title">Change for the best</h2>
      <p class="value-text">We strive to constantly grow and improve, both personally and professionally. We own up to our mistakes and strive to resolve and learn from them. We actively seek feedback from our clients and each other. We believe the most innovative ideas come when we intentionally look for them.</p>
    </section>

    <section class="value value--family">
      <h2 class="value-title">Family</h2>
      <p class="value-text">We are a family-owned business, and we consider everyone who works here and every one we serve to be part of the family. Being honest and genuine with each other and our customers is what sets us apart. We put ourselves in our customer’s shoes and make recommendations as if it were our chimney, our home and our family.</p>
    </section>

    <div class="company-name">
      <span class="company-name__square" aria-hidden="true"></span>
      <span class="company-name__text">Hearthwell Partners Inc</span>
    </div>

    <div class="torch-art" role="img" aria-label="Illustration of a hand raising a golden torch with a bright flame"></div>
  </main>
</body>
</html>
```